Tavolin brise

i am a designer who works with home-based business. i want to give surprise to my sister with describing a luxurious display at her blog.
two days later she would be birthday

Business

```html
<!DOCTYPE html>
<html lang="en">
<head>
<meta charset="utf-8">
<title>Tavolin brise</title>
<link href="https://fonts.googleapis.com/css2?family=Niconne&family=PT+Sans:wght@400;700&display=swap" rel="stylesheet">
<style>
  :root {
    --wood-light: #d08a26;
    --wood-mid: #8a4416;
    --wood-dark: #3a1808;
    --wood-deep: #1e0a04;
    --panel: #1a0b05;
    --gold: #f0b43c;
    --gold-deep: #c98a12;
    --heading: #f2c160;
    --text: #f3e6d6;
    --white: #ffffff;
    --nav-active: #5a2a0a;
    --nav: #b45c16;
    --nav-edge: #e6a54a;
    --footer: #140604;
    --smiles: #f07a18;
    --sunshine: #f6c12a;
    --love: #e0141a;
    --laughter: #4fb82c;
  }
  * { box-sizing: border-box; margin: 0; padding: 0; }
  html, body { width: 1037px; height: 1200px; overflow: hidden; background: var(--wood-deep); }
  body { font-family: "PT Sans", sans-serif; color: var(--text); }
  .page {
    position: relative; width: 1037px; height: 1200px; overflow: hidden;
    background:
      repeating-linear-gradient(90deg, rgba(0,0,0,0) 0 88px, rgba(0,0,0,.18) 88px 90px),
      linear-gradient(180deg, var(--wood-light) 0%, #b8651c 22%, var(--wood-mid) 40%, var(--wood-dark) 65%, #2a1006 92%);
  }
  .abs { position: absolute; }

  .brand { left: 57px; top: 40px; font-size: 42px; font-weight: 400; color: var(--white); letter-spacing: .5px; }

  .social { display: flex; gap: 10px; align-items: center; }
  .social-top { right: 22px; top: 18px; }
  .social-foot { right: 22px; top: 1126px; }
  .social-item { display: flex; align-items: center; gap: 5px; font-size: 13px; font-weight: 700; color: var(--white); }
  .social-item i { display: block; width: 12px; height: 12px; background: var(--gold); border-radius: 2px; }

  .main-nav { left: 417px; top: 79px; display: flex; gap: 6px; }
  .main-nav a {
    display: block; width: 98px; height: 35px; line-height: 33px; text-align: center;
    color: var(--white); text-decoration: none; font-size: 17px;
    background: linear-gradient(180deg, #c8701e, var(--nav) 55%, #96460e);
    border: 2px solid var(--nav-edge); border-radius: 11px;
  }
  .main-nav a.active { background: linear-gradient(180deg, #6e340e, var(--nav-active)); border-color: #c98a3a; }

  .side-tab {
    right: -6px; top: 148px; width: 64px; height: 68px;
    background: #3a2a20; border: 4px solid #9a9a9a; border-radius: 12px 0 0 12px;
    display: flex; align-items: center; justify-content: center;
  }

  .portrait-back { left: 34px; top: 118px; width: 232px; height: 370px; background: var(--gold); transform: rotate(-4deg); }
  .portrait { left: 57px; top: 127px; width: 218px; height: 361px; border: 3px solid var(--white);
    background: linear-gradient(160deg, #f6efe8 0%, #d9b9a0 35%, #6e4a3a 65%, #2a2220 100%); }

  .slider { left: 328px; top: 127px; width: 686px; height: 350px;
    background: radial-gradient(ellipse at 75% 70%, #2e160a 0%, var(--panel) 60%, #120704 100%); }
  .quote { left: 87px; top: 55px; width: 380px; font-family: "Niconne", cursive; font-size: 35px; line-height: 49px; color: var(--white); }
  .quote .smiles { color: var(--smiles); }
  .quote .sunshine { color: var(--sunshine); }
  .quote .love { color: var(--love); }
  .quote .laughter { color: var(--laughter); }
  .cake-photo { left: 439px; top: 165px; width: 228px; height: 168px; border-radius: 4px;
    background: radial-gradient(ellipse at 50% 55%, rgba(150,82,28,.55) 0%, rgba(70,34,12,.4) 55%, rgba(26,11,5,0) 100%); }
  .dots { left: 45px; top: 311px; display: flex; gap: 14px; }
  .dots span { width: 10px; height: 10px; border-radius: 50%; background: var(--gold); }
  .dots span.on { background: var(--white); }

  .section-title { font-family: "Niconne", cursive; font-size: 40px; color: var(--heading); font-weight: 400; }

  .about { left: 0; top: 522px; width: 693px; height: 236px; background: rgba(30,10,3,.45); border-radius: 0 8px 8px 0; }
  .about .section-title { position: absolute; left: 26px; top: 8px; }
  .about-photo-back { left: 18px; top: 78px; width: 150px; height: 136px; background: var(--gold); transform: rotate(12deg); border-radius: 6px; }
  .about-photo { left: 28px; top: 82px; width: 136px; height: 128px; border-radius: 6px;
    background: linear-gradient(135deg, #cfe4f0 0%, #9a8070 45%, #2a1e1c 70%, #e6d4c8 100%); }
  .about p { position: absolute; left: 181px; top: 76px; width: 492px; font-size: 14px; line-height: 25px; }

  .news .section-title { position: absolute; left: 716px; top: 524px; }
  .news-item { left: 706px; width: 320px; height: 82px; }
  .news-date { position: absolute; left: 0; top: 0; width: 70px; height: 70px; border-radius: 50%;
    background: radial-gradient(circle at 45% 35%, #f7cf3c, var(--gold-deep) 70%);
    border: 5px solid rgba(120,80,50,.85); color: #3a1a06; text-align: center; font-size: 16px; line-height: 19px; padding-top: 11px; }
  .news-item p { position: absolute; left: 83px; top: -10px; width: 220px; font-size: 14px; line-height: 25px; }

  .projects-title { left: 38px; top: 754px; }
  .project { width: 240px; }
  .project-back { position: absolute; left: 6px; top: -8px; width: 218px; height: 182px; background: var(--gold); transform: rotate(4deg); }
  .project-photo { position: absolute; left: 0; top: 0; width: 221px; height: 175px;
    background: linear-gradient(180deg, #f4e8e0 0%, #e9b9a8 35%, #c9d6b0 60%, #f4f2ee 100%); }
  .project-more { position: absolute; left: 0; bottom: 0; width: 221px; height: 43px; background: rgba(20,20,20,.6);
    color: var(--white); font-size: 22px; line-height: 43px; padding-left: 22px; }
  .project p { position: absolute; left: -5px; top: 195px; width: 220px; font-size: 14px; line-height: 25px; }

  .footer { left: 0; top: 1104px; width: 1037px; height: 96px; background: var(--footer); border-top: 1px solid #6a4a3a; }
  .footer-nav { left: 37px; top: 1120px; display: flex; gap: 36px; }
  .footer-nav a { color: var(--white); text-decoration: none; font-size: 14px; }
  .copyright { right: 37px; top: 1166px; font-size: 12px; color: var(--white); }
</style>
</head>
<body>
<div class="page">

  <div class="abs brand">Tavolin brise</div>

  <div class="abs social social-top">
    <span class="social-item"><i></i>Facet</span>
    <span class="social-item"><i></i>Chirp</span>
    <span class="social-item"><i></i>Feed</span>
  </div>

  <nav class="abs main-nav">
    <a class="active" href="#">Home</a>
    <a href="#">My Blog</a>
    <a href="#">Photos</a>
    <a href="#">Friends</a>
    <a href="#">Contacts</a>
  </nav>

  <div class="abs side-tab">
    <svg width="36" height="32" viewBox="0 0 36 32" aria-hidden="true">
      <rect x="2" y="10" width="32" height="20" fill="#f2c12a" stroke="#8a5a10" stroke-width="1.5"/>
      <path d="M2 10 L18 1 L34 10" fill="#f7d64a" stroke="#8a5a10" stroke-width="1.5"/>
      <path d="M2 10 L18 21 L34 10" fill="none" stroke="#8a5a10" stroke-width="1.5"/>
    </svg>
  </div>

  <div class="abs portrait-back"></div>
  <div class="abs portrait" role="img" aria-label="Portrait photo of a young woman in a straw hat and dark top"></div>

  <section class="abs slider">
    <p class="abs quote">"May your birthday be filled with <span class="smiles">smiles</span>, <span class="sunshine">sunshine</span>, <span class="love">love</span>, and <span class="laughter">laughter</span>."</p>
    <div class="abs cake-photo" role="img" aria-label="Photo of a birthday cake with lit candles"></div>
    <div class="abs dots"><span class="on"></span><span></span><span></span></div>
  </section>

  <section class="abs about">
    <h2 class="section-title">About Me</h2>
    <div class="abs about-photo-back"></div>
    <div class="abs about-photo" role="img" aria-label="Photo of a woman seen from behind at the beach"></div>
    <p>Lorem Ipsum is simply dummy text of the printing and typesetting industry. Lorem Ipsum has been the industry's standard dummy text.There are many variations of passages of Lorem Ipsum available, but the majority have suffered alteration in some form, by injected humour, or randomised words which don't look even slightly believable.</p>
  </section>

  <section class="news">
    <h2 class="section-title">Latest News</h2>
    <div class="abs news-item" style="top:588px;">
      <div class="news-date">Dec<br>22</div>
      <p>Lorem Ipsum is&nbsp; simply dummy text of the printing and typesetting industry.</p>
    </div>
    <div class="abs news-item" style="top:682px;">
      <div class="news-date">Dec<br>22</div>
      <p>Lorem Ipsum is&nbsp; simply dummy text of the printing and typesetting industry.</p>
    </div>
  </section>

  <h2 class="abs section-title projects-title">Latest Projects</h2>

  <div class="abs project" style="left:92px; top:821px;">
    <div class="project-back"></div>
    <div class="project-photo" role="img" aria-label="Photo of a bouquet of pastel roses in white paper">
      <div class="project-more">View More Dtails</div>
    </div>
    <p>Lorem Ipsum is&nbsp; simply dummy text of the printing and typesetting industry.</p>
  </div>
  <div class="abs project" style="left:415px; top:821px;">
    <div class="project-back"></div>
    <div class="project-photo" role="img" aria-label="Photo of a bouquet of pastel roses in white paper"></div>
    <p>Lorem Ipsum is&nbsp; simply dummy text of the printing and typesetting industry.</p>
  </div>
  <div class="abs project" style="left:730px; top:821px;">
    <div class="project-back"></div>
    <div class="project-photo" role="img" aria-label="Photo of a bouquet of pastel roses in white paper"></div>
    <p>Lorem Ipsum is&nbsp; simply dummy text of the printing and typesetting industry.</p>
  </div>

  <footer class="abs footer"></footer>
  <nav class="abs footer-nav">
    <a href="#">Home</a>
    <a href="#">My Blog</a>
    <a href="#">Photos</a>
    <a href="#">Friends</a>
    <a href="#">Contacts</a>
  </nav>
  <div class="abs social social-foot">
    <span class="social-item"><i></i>Facet</span>
    <span class="social-item"><i></i>Chirp</span>
    <span class="social-item"><i></i>Feed</span>
  </div>
  <p class="abs copyright">Copyright © 2011. www.tavolinbrise.com</p>

</div>
</body>
</html>
```